Telecommunications/Power civil contractor needs business card design

Were a new telecommunications/power underground civil contractor that is looking for a new business card design. Our company colours are silver or grey and orange. Feel free to use the white background logo or the black background logo.

Target Market(s)

Local contractors, utility companies, private sector mining/energy companies, developers.

Industry/Entity Type

Telecommunications

Contact Information for Business Card

Each card will need the following info:
Persons name:
Title:
E-mail:
Phone number:
Shop Address:
Mailing Address:

Requirements
Must have
• Each card will need the following info:
• Persons name:
• Title:
• E-mail:
• Phone number:
• Shop Address:
• Mailing Address:

```html
<!DOCTYPE html>
<html lang="en">
<head>
<meta charset="utf-8">
<title>Ridgeline Contracting Inc – Business Card</title>
<link rel="stylesheet" href="https://fonts.googleapis.com/css2?family=Saira:wght@500;700&family=Roboto:wght@400&display=swap">
<style>
  :root {
    --bg: #7d7f80;
    --card: #f7f7f5;
    --orange: #d9532a;
    --grey: #6e6e6e;
    --text: #5a5a5a;
  }
  * { margin: 0; padding: 0; box-sizing: border-box; }
  html, body { width: 1200px; height: 814px; overflow: hidden; }
  body {
    background: var(--bg);
    display: flex;
    align-items: center;
    justify-content: center;
    gap: 60px;
    font-family: "Roboto", Arial, sans-serif;
  }
  .card {
    position: relative;
    width: 525px;
    height: 300px;
    background: var(--card);
    box-shadow: 0 6px 18px rgba(0,0,0,.25);
    overflow: hidden;
  }
  .brand {
    display: flex;
    align-items: center;
    gap: 10px;
  }
  .brand-dot {
    width: 34px; height: 34px;
    border-radius: 50%;
    background: var(--orange);
    flex: none;
  }
  .brand-name {
    font-family: "Saira", Arial, sans-serif;
    font-weight: 700;
    color: var(--orange);
    text-transform: uppercase;
    line-height: 1.05;
    font-size: 17px;
    letter-spacing: .5px;
  }
  .card-front .brand { position: absolute; left: 34px; top: 32px; }
  .contact {
    position: absolute;
    left: 34px;
    top: 100px;
    list-style: none;
    color: var(--text);
    font-size: 12.5px;
    line-height: 19px;
  }
  .contact li { display: flex; align-items: center; gap: 8px; }
  .contact .address { padding-left: 20px; }
  .contact svg { width: 12px; height: 12px; flex: none; }
  .person {
    position: absolute;
    right: 34px;
    bottom: 40px;
    text-align: right;
  }
  .person-name {
    font-family: "Saira", Arial, sans-serif;
    font-weight: 700;
    font-size: 19px;
    color: var(--orange);
    letter-spacing: .5px;
  }
  .person-title {
    font-family: "Saira", Arial, sans-serif;
    font-weight: 500;
    font-size: 14px;
    color: var(--grey);
    letter-spacing: .5px;
  }
  .edge-tab {
    position: absolute;
    right: -14px;
    bottom: 44px;
    width: 28px; height: 28px;
    border-radius: 50%;
    background: var(--orange);
  }
  .card-back .brand {
    position: absolute;
    right: 40px;
    bottom: 44px;
  }
  .card-back .brand-dot { width: 46px; height: 46px; }
  .card-back .brand-name { font-size: 20px; }
</style>
</head>
<body>
  <section class="card card-front">
    <div class="brand">
      <span class="brand-dot"></span>
      <span class="brand-name">Ridgeline<br>Contracting Inc</span>
    </div>
    <ul class="contact">
      <li class="address">1420 Birchwood Road</li>
      <li class="address">Kettle Bay, Alaska 99871</li>
      <li>
        <svg viewBox="0 0 12 12" aria-hidden="true"><circle cx="6" cy="6" r="6" fill="#d9532a"/><path d="M4 3.2c.4-.3.8-.2 1 .2l.4.8c.1.3 0 .5-.2.7l-.3.2c.3.7.8 1.2 1.5 1.5l.2-.3c.2-.2.4-.3.7-.2l.8.4c.4.2.5.6.2 1l-.3.4c-2 .6-4.6-2-4-4z" fill="#fff"/></svg>
        555 214 0987
      </li>
      <li>
        <svg viewBox="0 0 12 12" aria-hidden="true"><circle cx="6" cy="6" r="6" fill="#d9532a"/><rect x="3" y="4" width="6" height="4.2" fill="none" stroke="#fff" stroke-width=".9"/><path d="M3 4l3 2.3L9 4" fill="none" stroke="#fff" stroke-width=".9"/></svg>
        dana@ridgelinecivil.com
      </li>
      <li>
        <svg viewBox="0 0 12 12" aria-hidden="true"><circle cx="6" cy="6" r="6" fill="#d9532a"/><circle cx="6" cy="6" r="3" fill="none" stroke="#fff" stroke-width=".8"/><path d="M3 6h6M6 3c-1.4 1.6-1.4 4.4 0 6M6 3c1.4 1.6 1.4 4.4 0 6" fill="none" stroke="#fff" stroke-width=".7"/></svg>
        www.ridgelinecivil.com
      </li>
    </ul>
    <div class="person">
      <div class="person-name">DANA WHITLOW</div>
      <div class="person-title">CEO / FOUNDER</div>
    </div>
    <span class="edge-tab"></span>
  </section>

  <section class="card card-back">
    <div class="brand">
      <span class="brand-dot"></span>
      <span class="brand-name">Ridgeline<br>Contracting Inc</span>
    </div>
  </section>
</body>
</html>
```